A5 size flyer for IT Company doing platform migrations

I need an A5 sized flyer for an IT company who specialise in platform migrations i.e. from one platform such as Halvex Teamgrid to another platform such as Corvane 480. The colours should be inline with what has been used in the attached logo file. The flyer is to be used in business shows that we attend and should be professional looking, be brief and to the point. The artwork should be IT platform migration related.

Target Market(s)

Other businesses

Colors
0054AA
0677BA
7BADD7
CADEEF
E8F1F8

```html
<!DOCTYPE html>
<html lang="en">
<head>
<meta charset="utf-8">
<title>Northpeak IT Ltd – Platform Migrations Flyer</title>
<link href="https://fonts.googleapis.com/css2?family=Montserrat:wght@400;500;600;700;800&display=swap" rel="stylesheet">
<style>
:root{
  --navy:#0054AA;
  --blue:#0677BA;
  --sky:#7BADD7;
  --mist:#CADEEF;
  --ice:#E8F1F8;
  --royal:#1f4fc4;
  --azure:#2f86e6;
  --cyan:#3fd0f2;
  --page:#a3a6f2;
  --ink:#2a3a55;
  --white:#ffffff;
}
*{box-sizing:border-box;margin:0;padding:0}
html,body{width:1200px;height:903px;overflow:hidden}
body{background:var(--page);font-family:"Montserrat",Arial,sans-serif;position:relative}
.flyer{position:absolute;left:296px;top:22px;width:608px;height:860px;background:var(--white);overflow:hidden;box-shadow:0 18px 40px rgba(40,40,120,.25)}
.hero{position:absolute;left:0;top:0;width:608px;height:520px;
  background:radial-gradient(circle at 50% 60%,#4fb0ff 0%,rgba(79,176,255,0) 45%),linear-gradient(160deg,var(--royal) 0%,var(--azure) 60%,#2a6fd6 100%)}
.brand{position:absolute;top:70px;left:0;width:100%;display:flex;justify-content:center;align-items:center;gap:8px}
.brand-mark{width:12px;height:12px;background:var(--white)}
.brand-name{color:var(--white);font-weight:500;font-size:17px;letter-spacing:.5px}
.headline{position:absolute;top:112px;left:0;width:100%;text-align:center;color:var(--white);font-weight:800;font-size:30px;line-height:1.15;text-shadow:0 2px 8px rgba(0,40,120,.35)}
.artwork{position:absolute;left:144px;top:210px;width:320px;height:200px;border-radius:50%;
  background:radial-gradient(ellipse at center,#cfe9ff 0%,#7bb8f2 40%,rgba(63,120,230,0) 72%)}
.bands{position:absolute;left:0;top:380px;width:608px;height:200px}
.why{position:absolute;left:40px;top:524px;width:420px;color:var(--navy);font-weight:700;font-size:24px;line-height:1.2}
.feature{position:absolute;width:270px;display:flex;gap:12px;align-items:flex-start}
.feature-icon{flex:0 0 44px;width:44px;height:44px;border:2px dotted var(--navy);border-radius:50%;display:flex;align-items:center;justify-content:center;margin-top:4px}
.feature-title{color:var(--blue);font-size:9px;font-weight:700;letter-spacing:1.6px;text-transform:uppercase;margin-bottom:3px}
.feature-text{color:var(--ink);font-size:12px;line-height:1.3}
.f1{left:34px;top:604px}
.f2{left:34px;top:692px}
.f3{left:316px;top:640px}
.f4{left:316px;top:716px}
.contact{position:absolute;left:0;bottom:0;width:608px;height:62px;background:linear-gradient(90deg,var(--blue),var(--navy) 70%,var(--blue));display:flex;align-items:center;justify-content:space-around;color:var(--white);font-size:13px;font-weight:600}
.contact-item{display:flex;align-items:center;gap:7px}
</style>
</head>
<body>
<main class="flyer">
  <section class="hero">
    <div class="brand"><span class="brand-mark"></span><span class="brand-name">Northpeak IT Ltd</span></div>
    <h1 class="headline">Your Trusted Partner for<br>Seamless Platform Migrations</h1>
    <div class="artwork" role="img" aria-label="Illustration of a desktop monitor and laptop exchanging files through a cloud, with foliage and floating document icons"></div>
  </section>

  <svg class="bands" viewBox="0 0 608 200" preserveAspectRatio="none" aria-hidden="true">
    <polygon points="0,70 60,40 608,40 608,200 0,200" fill="var(--white)"/>
    <polygon points="0,95 130,60 608,60 608,110 300,110 250,150 0,150" fill="var(--cyan)" opacity=".55"/>
    <polygon points="60,40 330,40 280,95 0,95 0,70" fill="#7fe0f7"/>
    <polygon points="330,100 608,100 608,140 300,140" fill="var(--sky)" opacity=".7"/>
    <rect x="0" y="140" width="608" height="60" fill="var(--white)"/>
  </svg>

  <h2 class="why">Why Choose Us for Your Platform Migration Needs?</h2>

  <div class="feature f1">
    <span class="feature-icon"><svg width="22" height="22" viewBox="0 0 22 22"><circle cx="11" cy="11" r="7" fill="none" stroke="var(--navy)" stroke-width="4" stroke-dasharray="3 2.5"/><circle cx="11" cy="11" r="5" fill="none" stroke="var(--navy)" stroke-width="3"/></svg></span>
    <div><p class="feature-title">Expertise and Experience:</p><p class="feature-text">Our team of skilled IT professionals has extensive experience in platform migrations.</p></div>
  </div>
  <div class="feature f2">
    <span class="feature-icon"><svg width="20" height="20" viewBox="0 0 20 20"><circle cx="8" cy="8" r="5.5" fill="none" stroke="var(--navy)" stroke-width="2.2"/><line x1="12" y1="12" x2="18" y2="18" stroke="var(--navy)" stroke-width="2.6" stroke-linecap="round"/></svg></span>
    <div><p class="feature-title">Tailored Solutions:</p><p class="feature-text">We offer customized migration solutions tailored to your specific need</p></div>
  </div>
  <div class="feature f3">
    <span class="feature-icon"><svg width="24" height="16" viewBox="0 0 24 16"><path d="M6 16a5 5 0 0 1-.6-10A7 7 0 0 1 18.5 6 5 5 0 0 1 18 16z" fill="var(--navy)"/></svg></span>
    <div><p class="feature-title">Seamless Data Migration:</p><p class="feature-text">Your data is invaluable, and we prioritize its secure transfer.</p></div>
  </div>
  <div class="feature f4">
    <span class="feature-icon"><svg width="20" height="18" viewBox="0 0 20 18"><path d="M2 2h16v10H9l-4 4v-4H2z" fill="none" stroke="var(--navy)" stroke-width="2" stroke-linejoin="round"/></svg></span>
    <div><p class="feature-title">Ongoing Support:</p><p class="feature-text">We're committed to your success even after the migration is complete.</p></div>
  </div>

  <footer class="contact">
    <span class="contact-item"><svg width="11" height="15" viewBox="0 0 11 15"><path d="M5.5 0A5.5 5.5 0 0 0 0 5.5C0 9.5 5.5 15 5.5 15S11 9.5 11 5.5A5.5 5.5 0 0 0 5.5 0zm0 7.5a2 2 0 1 1 0-4 2 2 0 0 1 0 4z" fill="var(--white)"/></svg>214 Harbour Lane</span>
    <span class="contact-item"><svg width="15" height="11" viewBox="0 0 15 11"><rect x="0" y="0" width="15" height="11" fill="var(--white)"/><polyline points="0,0 7.5,6 15,0" fill="none" stroke="var(--navy)" stroke-width="1.3"/></svg>hello@northpeakit.com</span>
    <span class="contact-item"><svg width="13" height="13" viewBox="0 0 24 24"><path d="M6.6 10.8a15.1 15.1 0 0 0 6.6 6.6l2.2-2.2a1 1 0 0 1 1-.25 11.4 11.4 0 0 0 3.6.6 1 1 0 0 1 1 1V20a1 1 0 0 1-1 1A17 17 0 0 1 3 4a1 1 0 0 1 1-1h3.5a1 1 0 0 1 1 1c0 1.250.2 2.45.6 3.6a1 1 0 0 1-.25 1z" fill="var(--white)"/></svg>390-000-4817</span>
  </footer>
</main>
</body>
</html>
```